Business Card Design

Take existing logo/brand and develop business card for sales team.
We have two separate brands and require a business card for each.

1. VoxHarbor
2. MyNimbusLinko

Refer to our websites www.voxharbor.example.au and www.mynimbuslinko.example.au for designs currently implemented and in the marketplace.

Both cards are brands of our parent company Quorra Systems Pty Ltd - an Australian Telecommunications company in the medium business sector. We have only business customers, no retail/residential consumers.

Target Market(s)

Australian Business - small to medium enterprise

Industry/Entity Type

Business

Contact Information for Business Card

Lev Dorrit
Sales Director
Mobile: +61 400 555 187
Direct: +61 3 9555 0137
Email: lev@voxharbor.example.au
VoxHarbor (a brand of Quorra Systems Pty Ltd)

Lev Dorrit
Sales Director
Mobile: +61 400 555 187
Direct: +61 3 9555 0137
Email: lev@mynimbuslinko.example.au
MyNimbusLinko (a brand of Quorra Systems Pty Ltd)

Font styles to use
Sans Serif
Other font styles liked:
• Roboto Condensed, Open Sans

Requirements
Must have
• Clean lines, crisp fonts - suggest Roboto Condensed or similar.
• Must be easy to read and clear.
• Brand colour #0C8CCD
• Two colour maximum
Nice to have
• Modern, intellectual and unique design.
Should not have
• No die cuts
• No copies or rip-offs of other designs

```html
<!DOCTYPE html>
<html lang="en">
<head>
<meta charset="utf-8">
<title>VoxHarbor and MyNimbusLinko business cards</title>
<link rel="stylesheet" href="https://fonts.googleapis.com/css2?family=Open+Sans:ital,wght@0,400;0,600;0,700;1,400&display=swap">
<style>
  :root {
    --brand-blue: #0c8ccd;
    --ink: #3a3a3c;
    --paper: #ffffff;
    --silver-light: #f4f4f4;
    --silver-mid: #dcdcdc;
    --silver-dark: #b9b9b9;
    --card-edge: #d0d0d0;
  }
  * { box-sizing: border-box; margin: 0; padding: 0; }
  html, body {
    width: 1200px; height: 759px; overflow: hidden;
    background: var(--paper);
    font-family: "Open Sans", Arial, sans-serif;
  }
  .sheet { position: relative; width: 1200px; height: 759px; }

  .card {
    position: absolute;
    width: 536px; height: 318px;
    border-radius: 22px;
    border: 1px solid var(--card-edge);
    background:
      radial-gradient(ellipse 62% 60% at 55% 55%, rgba(255,255,255,0.95) 0%, rgba(255,255,255,0.75) 55%, rgba(255,255,255,0) 80%),
      linear-gradient(90deg, var(--silver-dark) 0%, var(--silver-mid) 18%, var(--silver-light) 50%, var(--silver-mid) 82%, var(--silver-dark) 100%);
    box-shadow: 0 6px 10px rgba(0,0,0,0.18);
    overflow: hidden;
  }
  .card--vox-front    { left: 37px;  top: 47px; }
  .card--nimbus-front { left: 650px; top: 47px; }
  .card--vox-back     { left: 33px;  top: 410px; }
  .card--nimbus-back  { left: 645px; top: 410px; }

  /* wordmarks */
  .wordmark {
    position: absolute;
    display: flex; align-items: center;
    color: var(--ink);
    font-weight: 400;
    white-space: nowrap;
  }
  .wordmark__dot { background: var(--brand-blue); flex: none; }
  .wordmark__dot--circle { border-radius: 50%; }

  .front-mark { left: 0; right: 0; top: 108px; justify-content: center; font-size: 50px; gap: 18px; }
  .front-mark .wordmark__dot { width: 74px; height: 74px; }
  .front-url {
    position: absolute; left: 0; right: 0; top: 208px;
    text-align: center;
    color: var(--brand-blue);
    font-family: Arial, "Open Sans", sans-serif;
    font-weight: 700; font-size: 22px;
  }

  .back-mark { left: 18px; top: 26px; font-size: 34px; gap: 10px; }
  .back-mark .wordmark__dot { width: 48px; height: 48px; }

  .contact { position: absolute; left: 178px; top: 92px; }
  .contact__name { color: var(--brand-blue); font-weight: 700; font-size: 21px; line-height: 26px; }
  .contact__role { color: var(--ink); font-size: 16px; line-height: 22px; margin-bottom: 12px; }
  .contact__list { list-style: none; }
  .contact__item {
    display: flex; align-items: center; gap: 9px;
    color: var(--ink); font-size: 15.5px; line-height: 23.5px;
  }
  .contact__icon { width: 16px; height: 16px; flex: none; stroke: var(--ink); fill: none; stroke-width: 1.4; }

  .card__footer {
    position: absolute; left: 0; right: 0; top: 262px;
    text-align: center;
    color: var(--brand-blue);
    font-style: italic; font-size: 14px;
  }
</style>
</head>
<body>
<main class="sheet">

  <section class="card card--vox-front" aria-label="VoxHarbor card front">
    <div class="wordmark front-mark"><span class="wordmark__dot wordmark__dot--circle"></span>VoxHarbor</div>
    <p class="front-url">www.voxharbor.example.au</p>
  </section>

  <section class="card card--nimbus-front" aria-label="MyNimbusLinko card front">
    <div class="wordmark front-mark"><span class="wordmark__dot"></span>MyNimbusLinko</div>
    <p class="front-url">www.mynimbuslinko.example.au</p>
  </section>

  <section class="card card--vox-back" aria-label="VoxHarbor card back">
    <div class="wordmark back-mark"><span class="wordmark__dot wordmark__dot--circle"></span>VoxHarbor</div>
    <div class="contact">
      <p class="contact__name">Lev Dorrit</p>
      <p class="contact__role">Sales Director</p>
      <ul class="contact__list">
        <li class="contact__item"><svg class="contact__icon" viewBox="0 0 16 16"><rect x="4" y="1.5" width="8" height="13" rx="1.5"/><line x1="7" y1="12" x2="9" y2="12"/></svg>+61 400 555 187</li>
        <li class="contact__item"><svg class="contact__icon" viewBox="0 0 16 16"><path d="M4 1.5 L6.5 4.5 L5 6.5 Q7 10 9.5 11 L11.5 9.5 L14.5 12 L12.5 14.5 Q4 13 1.5 4 Z" fill="var(--ink)" stroke="none"/></svg>+61 3 9555 0137</li>
        <li class="contact__item"><svg class="contact__icon" viewBox="0 0 16 16"><rect x="1.5" y="3.5" width="13" height="9"/><path d="M1.5 3.5 L8 9 L14.5 3.5"/></svg>lev@voxharbor.example.au</li>
        <li class="contact__item"><svg class="contact__icon" viewBox="0 0 16 16"><circle cx="8" cy="8" r="6.5"/><ellipse cx="8" cy="8" rx="3" ry="6.5"/><line x1="1.5" y1="8" x2="14.5" y2="8"/></svg>www.voxharbor.example.au</li>
      </ul>
    </div>
    <p class="card__footer">VoxHarbor (a brand of Quorra Systems Pty Ltd)</p>
  </section>

  <section class="card card--nimbus-back" aria-label="MyNimbusLinko card back">
    <div class="wordmark back-mark"><span class="wordmark__dot"></span>MyNimbusLinko</div>
    <div class="contact">
      <p class="contact__name">Lev Dorrit</p>
      <p class="contact__role">Sales Director</p>
      <ul class="contact__list">
        <li class="contact__item"><svg class="contact__icon" viewBox="0 0 16 16"><rect x="4" y="1.5" width="8" height="13" rx="1.5"/><line x1="7" y1="12" x2="9" y2="12"/></svg>+61 400 555 187</li>
        <li class="contact__item"><svg class="contact__icon" viewBox="0 0 16 16"><path d="M4 1.5 L6.5 4.5 L5 6.5 Q7 10 9.5 11 L11.5 9.5 L14.5 12 L12.5 14.5 Q4 13 1.5 4 Z" fill="var(--ink)" stroke="none"/></svg>+61 3 9555 0137</li>
        <li class="contact__item"><svg class="contact__icon" viewBox="0 0 16 16"><rect x="1.5" y="3.5" width="13" height="9"/><path d="M1.5 3.5 L8 9 L14.5 3.5"/></svg>lev@mynimbuslinko.example.au</li>
        <li class="contact__item"><svg class="contact__icon" viewBox="0 0 16 16"><circle cx="8" cy="8" r="6.5"/><ellipse cx="8" cy="8" rx="3" ry="6.5"/><line x1="1.5" y1="8" x2="14.5" y2="8"/></svg>www.mynimbuslinko.example.au</li>
      </ul>
    </div>
    <p class="card__footer">MyNimbusLinko (a brand of Quorra Systems Pty Ltd)</p>
  </section>

</main>
</body>
</html>
```